We are a organisation that provide outdoor adventure based tours to international students in New Ze

We are a Waikato New Zealand based company that runs adventure and outdoor tours around New Zealand. Activities included in our tours are mountain biking, rafting, sea kayaking, surfing/SUPing, luge, high ropes course, tramping, snorkelling and cultural activities. We need a Name/Logo, advertisement and information Flyers that we can give to the students/customers ASAP. We still haven't come up with a name so are hoping that designers can be more creative than we are. we are running our fist trip Dec 15th-22nd 2013.

Attached are some bits of information that we need to be included in the flyer. We need to get the 'Brightwater Tour' filled up first and the 'Kerrin's Shell Tour' will be later.

We want it to be an exciting and edgy design with an 'outdoor' feel to it. There is the potential for this design to be expanded into our website.

The brochure/ Flyer can come in any creative format.

Target Market(s)

High school aged students. We will be expanding to University students in the future. We also need to make sure that this is appealing to the parents. It will be them who will agree to them going on the trips after all.

Industry/Entity Type

It Company

Requirements
Must have
• Our Contact details.
Booking Info
Tour information from attached.
Nice to have
• Photos can use the ones we have put into the attachment or other images from the outdoors that designers can source to make it look good.

```html
<!DOCTYPE html>
<html lang="en">
<head>
<meta charset="utf-8">
<title>New Zealand Tours – Flyers</title>
<link rel="stylesheet" href="https://fonts.googleapis.com/css2?family=Orbitron:wght@800&family=Lato:wght@400;700&family=Kaushan+Script&display=swap">
<style>
:root{
  --navy:#0d2a66;
  --navy-deep:#091d4a;
  --navy-mid:#1a3f86;
  --yellow:#f6c900;
  --yellow-text:#f4d21e;
  --white:#ffffff;
  --ink:#1b1b1b;
  --backdrop:#d9d9d9;
  --sea:#2d5f92;
  --sky:#a9c3d8;
}
*{box-sizing:border-box;margin:0;padding:0}
html,body{width:1200px;height:801px;overflow:hidden}
body{background:var(--backdrop);font-family:'Lato',sans-serif;position:relative}
.flyer{position:absolute;background:var(--navy);overflow:hidden;box-shadow:0 2px 8px rgba(0,0,0,.25)}
.flyer--intro{left:20px;top:25px;width:568px;height:750px;
  background:linear-gradient(180deg,var(--navy-mid) 0%,var(--navy) 45%,var(--navy-deep) 100%)}
.flyer--tour{left:598px;top:25px;width:570px;height:735px;
  background:linear-gradient(180deg,var(--navy-mid) 0%,var(--navy) 40%,var(--navy-deep) 100%)}
.abs{position:absolute}
.title{font-family:'Orbitron',sans-serif;font-weight:800;color:var(--navy);font-size:30px;letter-spacing:2px;text-align:center;width:100%}
.hero-sea{left:0;top:50px;width:100%;height:185px;
  background:linear-gradient(180deg,var(--sky) 0%,#5d87ad 35%,var(--sea) 60%,var(--navy) 100%)}
.hero-cove{left:0;top:60px;width:100%;height:140px;
  background:linear-gradient(180deg,#c9d9e4 0%,#6f9472 45%,#4d7fa3 70%,var(--navy) 100%)}
.lead{left:18px;top:204px;width:292px;color:var(--yellow-text);font-weight:700;font-size:14.5px;line-height:19px}
.lead span{display:block;white-space:nowrap}
.lead .full{text-align:justify;text-align-last:justify}
.body-copy{color:var(--white);font-size:10.5px;line-height:13px;text-align:justify}
.tagline{font-family:'Kaushan Script',cursive;color:var(--white);font-size:20px}
.question-box{left:322px;top:238px;width:224px;height:104px;background:var(--yellow);border-radius:6px;padding:8px 6px;font-size:12.5px;color:var(--ink)}
.question-box li{list-style:none;display:flex;gap:5px;margin-bottom:7px;line-height:14px}
.question-box li::before{content:"";flex:none;width:11px;height:11px;border-radius:50%;background:var(--navy);margin-top:2px}
.card{background:var(--white);border-radius:6px;color:var(--ink)}
.platform{left:325px;top:352px;width:230px;height:295px;padding:12px;font-size:10.5px;line-height:12.5px}
.platform h3{font-style:italic;font-size:13px;line-height:14px;margin-bottom:12px}
.platform ol{padding-left:16px;margin-bottom:10px}
.platform p{margin-bottom:10px}
.snap{border:5px solid var(--white);box-shadow:0 2px 6px rgba(0,0,0,.4)}
.footer-text{left:0;top:682px;width:100%;text-align:center;font-family:'Kaushan Script',cursive;color:var(--navy);font-size:30px}
.yellow-script{font-family:'Kaushan Script',cursive;color:var(--yellow-text);font-size:17px;line-height:22px}
.yellow-head{color:var(--yellow-text);font-weight:700;font-size:12px}
.list{color:var(--white);font-size:11px;line-height:12.8px;list-style:none}
.days{left:247px;top:295px;width:307px;height:360px;padding:8px 10px;font-size:10.5px;line-height:12.5px}
.days h3{color:var(--navy);font-size:12.5px;line-height:14px;margin-bottom:10px}
.days p{color:var(--navy);margin-bottom:10px}
.days b{font-style:italic}
.contact{left:20px;top:582px;width:210px;font-size:10px;line-height:12px;color:var(--ink)}
.contact .name{color:var(--navy);font-weight:700;margin-top:12px}
</style>
</head>
<body>

<section class="flyer flyer--intro" aria-label="New Zealand Tours flyer">
  <div class="abs hero-sea" role="img" aria-label="Snorkeller in the sea with a charter boat behind"></div>
  <svg class="abs" style="left:0;top:0" width="568" height="80" viewBox="0 0 568 80"><path d="M0 0H568V48Q284 72 0 62Z" fill="#fff"/></svg>
  <h1 class="abs title" style="top:20px">NEW ZEALAND TOURS</h1>

  <p class="abs lead">
    <span class="full">We are the only adventure tour</span>
    <span class="full">organization providing exciting</span>
    <span>experiences on and off the beaten track</span>
  </p>
  <div class="abs tagline" style="left:330px;top:198px">Take the path less travelled</div>

  <div class="abs body-copy" style="left:18px;top:280px;width:288px">
    <p style="margin-bottom:10px">We are all about making your story in NZ one worth telling. Here at ..............Tours we pride ourselves in providing the most memorable and exciting adventure based tours for students JUST LIKE YOU. We don't just take you to some of New Zealand's world-class adventure activities, we also take you deeper into the real New Zealand other tours don't touch.</p>
    <p>Our guides are addicted to adventure and the outdoors. We are ready to have some fun and share with you our knowledge of our beautiful country. Come and get into it!</p>
  </div>

  <ul class="abs question-box">
    <li>Love the outdoors?</li>
    <li>Want some better stories about your NZ exchange?</li>
    <li>Check us out!!</li>
  </ul>

  <div class="abs card platform">
    <h3>Our tours offer a platform for foreign students to ...</h3>
    <ol>
      <li>Build confidence</li>
      <li>Create positive relationships</li>
      <li>Experience new cultures</li>
      <li>Solve problems in an unfamiliar and challenging outdoor environment</li>
    </ol>
    <p>Our tours have many great popular NZ tourist activities but more importantly go where no other similar tours go. We create our own path less travelled!!!</p>
    <p>We also aim to keep driving/travel to a minumum. Through experience we know this means more time having fun ; )</p>
    <p>Sound good?...Check out our new Tours on Offer........</p>
  </div>

  <div class="abs snap" style="left:18px;top:430px;width:210px;height:140px;transform:rotate(-3deg);background:linear-gradient(160deg,#c8d0c8,#4b5a48)" role="img" aria-label="Walkers in steam at a geothermal stream"></div>
  <div class="abs snap" style="left:152px;top:455px;width:180px;height:140px;transform:rotate(-4deg);background:linear-gradient(180deg,#8fb3d8,#5f7fa0 55%,#5b5a4a)" role="img" aria-label="Group with kayaks on a lake shore"></div>
  <div class="abs snap" style="left:42px;top:545px;width:190px;height:150px;transform:rotate(-2deg);background:linear-gradient(180deg,#dfe6ea,#6c9fc0 45%,#3b6a3a)" role="img" aria-label="Bush-lined lake bay"></div>

  <svg class="abs" style="left:0;top:640px" width="568" height="110" viewBox="0 0 568 110"><path d="M0 40Q284 0 568 25V110H0Z" fill="var(--yellow)"/></svg>
  <div class="abs footer-text">Our fist trip Dec 15th-22nd 2013</div>
</section>

<section class="flyer flyer--tour" aria-label="Brightwater Tour flyer">
  <div class="abs hero-cove" role="img" aria-label="Sea arch and rock stack on a sandy beach"></div>
  <svg class="abs" style="left:0;top:0" width="570" height="90" viewBox="0 0 570 90"><path d="M0 0H570V58Q300 80 0 72Z" fill="#fff"/></svg>
  <h1 class="abs title" style="top:32px;font-size:28px">THE BRIGHTWATER TOUR</h1>

  <div class="abs yellow-script" style="left:37px;top:178px">Tour dates : Dec 15th -22nd</div>
  <div class="abs yellow-script" style="left:372px;top:186px">Limited to 30 spaces</div>

  <p class="abs body-copy" style="left:34px;top:212px;width:522px;line-height:12.5px">The Brightwater Tour is one of our most exciting adventure tours. We travel from the heart of the Waikato, home of the beautiful limestone caves, to Raglan the capital of NZ surfing on the west coast. We then make our way east to the adventure tourism playground of New Zealand, Rotorua! From there we hit the golden sands of Mt Maunganui. This culturally rich central Bay of Plenty region is home to some of our most exciting and beautiful rivers, mountains, forests and walks. Onto New Zealand's best kept secret the Coromandel!</p>

  <div class="abs yellow-head" style="left:32px;top:295px">Activities we have lined up for you:</div>
  <ul class="abs list" style="left:30px;top:311px">
    <li>21.Rafting</li><li>22.Mountain Biking</li><li>23.Surfing</li><li>24.Caving</li><li>25.Luge/Thrill Rides</li>
  </ul>
  <ul class="abs list" style="left:128px;top:311px">
    <li>26.Sea Kayaking</li><li>27.Tramping</li><li>28.High Ropes Course</li><li>29.Hot Pools</li><li>30.Tramping/Sight seeing</li><li>31.Cultural Experience</li>
  </ul>

  <div class="abs snap" style="left:27px;top:398px;width:216px;height:104px;border-radius:6px;background:radial-gradient(circle at 50% 60%,#f0a020 0%,#8a3a10 30%,#1c1410 70%)" role="img" aria-label="Students gathered around a campfire at night"></div>

  <div class="abs yellow-head" style="left:24px;top:514px">Included in the costs</div>
  <ul class="abs list" style="left:24px;top:533px">
    <li>32.Food</li><li>33.All transport</li><li>34.Cost of all activities and guides</li>
  </ul>

  <svg class="abs" style="left:0;top:578px" width="250" height="157" viewBox="0 0 250 157"><path d="M0 0H190Q225 0 235 40L250 157H0Z" fill="#fff"/></svg>
  <div class="abs contact">
    <p style="font-weight:700">Contact details –</p>
    <p>To make a booking contact either</p>
    <p class="name">Tane Walker</p>
    <p>tanewalker@mailbox.example</p>
    <p>0224417302</p>
    <p class="name">Oliver Grant</p>
    <p>olivergrant@mailbox.example</p>
    <p>0213390575</p>
  </div>

  <div class="abs card days">
    <h3>All of this, 8 days of fun and making memories with other international students for $1455pp</h3>
    <p><b>Day 1 –</b> Waikato high ropes course and Karamu/Waitomo Caving</p>
    <p><b>Day 2 –</b> Raglan camping surfing and Kayak Tours in the Whaingaroa Harbor</p>
    <p><b>Day 3 -</b> Travel to Rotorua Luge and Skyrides, tramp in Kaingaroa Forest/Whakarewarewa Thermal Village and Hot Pools</p>
    <p><b>Day 4 –</b> Rafting the famous Kaituna River and Mountain Bike the world-renowned Red Wood forests, cultural night</p>
    <p><b>Day 5 –</b> Travel to the Bay of Plenty and Climb the Mount Maunganui (Mauao), shopping and Harbour tour</p>
    <p><b>Day 6 –</b> Travel to Coromandle Cathedral Cove kayak tours and Hotwater Beach</p>
    <p><b>Day 7 -</b> Pinnalces tramp in Coromandle, Whangamata beach day</p>
    <p><b>Day 8 -</b> Back to Waikato, Hot pools in Te Aroha in the morning and farewells</p>
  </div>

  <div class="abs snap" style="left:398px;top:637px;width:112px;height:80px;background:linear-gradient(180deg,#9bb7cc,#6d6a4a 60%,#c9a02a)" role="img" aria-label="Group of students posing with rafts"></div>
</section>

</body>
</html>
```